You’re Cordially Invited
To a Sunset Celebration Honoring the Launch of The Calloway

Date: Thursday, May 15
Time: 5:30 PM – 7:30 PM
Location: The Calloway, 47 Marlow Lane, East Boston

Please join us for an elegant evening of connection and celebration as we unveil The Calloway Project.
Enjoy private tours of Units 3 and 4, along with our breathtaking roof deck offering sweeping views of East Boston at sunset.

Sip curated selections of beer and wine and savor light seasonal bites as you mingle with colleagues and guests.

Feel free to bring clients, friends, or family — all are welcome!

Kindly RSVP to:
Daria Whitfield, Sparrowgate Realty
📧 Daria@sparrowgatehomes.example

Please include logo, classic design, and attachments. Colors navy, gold, white

```html
<!DOCTYPE html>
<html lang="en">
<head>
<meta charset="utf-8">
<title>Sunset Celebration – The Calloway</title>
<link href="https://fonts.googleapis.com/css2?family=Cormorant+Garamond:ital,wght@1,500&family=DM+Serif+Display&family=Libre+Baskerville:ital@1&family=Mr+Dafoe&family=Playfair+Display:wght@800;900&family=Poppins:wght@400;500&display=swap" rel="stylesheet">
<style>
  :root {
    --navy-deep: #17254f;
    --navy: #1f3268;
    --navy-light: #3f6aa6;
    --sky: #5f92c8;
    --gold: #c9a04a;
    --gold-soft: #d8b262;
    --white: #ffffff;
    --page: #d9d9d9;
  }
  * { margin: 0; padding: 0; box-sizing: border-box; }
  html, body { width: 1200px; height: 751px; overflow: hidden; background: var(--page); }
  .canvas { position: relative; width: 1200px; height: 751px; }
  .invitation {
    position: absolute; left: 334px; top: 0; width: 532px; height: 751px; overflow: hidden;
    background:
      radial-gradient(ellipse 320px 260px at 470px 10px, var(--sky) 0%, rgba(95,146,200,0) 70%),
      radial-gradient(ellipse 300px 500px at 480px 360px, rgba(63,106,166,.35) 0%, rgba(63,106,166,0) 70%),
      linear-gradient(180deg, var(--navy) 0%, var(--navy) 60%, var(--navy-deep) 100%);
    color: var(--white);
    text-align: center;
  }
  .rsvp-band { position: absolute; left: 0; right: 0; top: 653px; bottom: 0; background: rgba(20,30,66,.55); }
  .frame { position: absolute; inset: 0; }
  .line { position: absolute; left: 0; width: 100%; line-height: 1; white-space: nowrap; }

  .brand-name { top: 118px; font-family: "DM Serif Display", serif; font-size: 30px; color: var(--gold); }

  .invite-lead { top: 218px; font-family: "Poppins", sans-serif; font-size: 12px; letter-spacing: 3.4px; }
  .title-sunset { top: 228px; font-family: "Playfair Display", serif; font-weight: 900; font-size: 74px; color: var(--gold); letter-spacing: -1px; }
  .title-script { top: 268px; font-family: "Mr Dafoe", cursive; font-size: 64px; color: var(--white); text-shadow: 0 2px 4px rgba(0,0,0,.45); }
  .title-honor { top: 328px; font-family: "Cormorant Garamond", serif; font-style: italic; font-weight: 500; font-size: 22px; }
  .title-project { top: 350px; font-family: "Playfair Display", serif; font-weight: 800; font-size: 34px; color: var(--gold); }

  .event-date { top: 418px; font-family: "DM Serif Display", serif; font-size: 27px; }
  .event-date sup { font-size: 14px; }
  .event-time { top: 463px; font-family: "DM Serif Display", serif; font-size: 22px; }
  .event-place { top: 488px; font-family: "Poppins", sans-serif; font-size: 12px; color: var(--gold-soft); line-height: 15px; }
  .event-copy { top: 530px; font-family: "Libre Baskerville", serif; font-style: italic; font-size: 7.2px; line-height: 11px; }
  .banner { position: absolute; left: 0; top: 563px; width: 532px; height: 26px; }
  .banner-text { top: 567px; font-family: "Libre Baskerville", serif; font-style: italic; font-size: 7.6px; line-height: 9px; color: var(--navy-deep); }
  .welcome { top: 609px; font-family: "Poppins", sans-serif; font-size: 11.5px; }
  .rsvp-label { top: 647px; font-family: "Poppins", sans-serif; font-size: 10px; }
  .host-name { top: 663px; font-family: "DM Serif Display", serif; font-size: 25px; color: var(--gold); }
  .host-company { top: 690px; font-family: "DM Serif Display", serif; font-size: 15px; }
  .host-email { top: 710px; font-family: "Poppins", sans-serif; font-size: 9px; }
</style>
</head>
<body>
<main class="canvas">
  <article class="invitation">
    <div class="rsvp-band"></div>

    <svg class="frame" width="532" height="751" viewBox="0 0 532 751" fill="none" stroke="#c9a04a" stroke-width="1">
      <path d="M34 20 H498 Q498 36 512 36 V715 Q498 715 498 731 H34 Q34 715 20 715 V36 Q34 36 34 20 Z"/>
      <path d="M113 268 H95 V392 H438 V268 H423"/>
      <line x1="138" y1="455" x2="396" y2="455"/>
      <circle cx="170" cy="455" r="2" fill="#c9a04a"/>
      <circle cx="362" cy="455" r="2" fill="#c9a04a"/>
      <line x1="20" y1="653" x2="221" y2="653" stroke="#c9c9d6"/>
      <line x1="311" y1="653" x2="512" y2="653" stroke="#c9c9d6"/>
    </svg>

    <svg class="banner" viewBox="0 0 532 26">
      <line x1="89" y1="13" x2="119" y2="13" stroke="#c9a04a"/>
      <line x1="412" y1="13" x2="442" y2="13" stroke="#c9a04a"/>
      <circle cx="89" cy="13" r="1.8" fill="#c9a04a"/>
      <circle cx="442" cy="13" r="1.8" fill="#c9a04a"/>
      <polygon points="119,13 130,2 402,2 412,13 402,24 130,24" fill="#c9a04a"/>
    </svg>

    <p class="line brand-name">Sparrowgate Realty</p>

    <p class="line invite-lead">You’re Cordially Invited to a</p>
    <h1 class="line title-sunset">SUNSET</h1>
    <p class="line title-script">Celebration</p>
    <p class="line title-honor">Honoring the Launch of</p>
    <h2 class="line title-project">THE CALLOWAY</h2>

    <p class="line event-date">Thursday, May 15<sup>th</sup></p>
    <p class="line event-time">5:30 PM – 7:30 PM</p>
    <p class="line event-place">The Calloway, 47 Marlow Lane,<br>East Boston</p>
    <p class="line event-copy">Please join us for an elegant evening of connection and celebration as we unveil The Calloway Project.<br>Enjoy private tours of Units 3 and 4, along with our breathtaking roof deck offering sweeping views of East Boston at sunset.</p>
    <p class="line banner-text">Sip curated selections of beer and wine and savor light seasonal<br>bites as you mingle with colleagues and guests.</p>
    <p class="line welcome">Feel free to bring clients, friends, or family — all are welcome!</p>

    <p class="line rsvp-label">Kindly RSVP to</p>
    <p class="line host-name">Daria Whitfield</p>
    <p class="line host-company">Sparrowgate Realty</p>
    <p class="line host-email">Daria@sparrowgatehomes.example</p>
  </article>
</main>
</body>
</html>
```